Ledgerwise 540 for Tavlo

We are looking to design a page for the mobile app. The app is intended for financial professionals and is based on a successful desktop application. The existing design will serve as a very rough guideline, but we are open to hearing ideas.
Uploaded file #1 contains a screenshot of the existing design. The workflow is as follows:
The user picks a portfolio from the Dropdown below portfolio.
The user picks a Loss Threshold, which will dictate what gets onto the bubble chart below.
Once the bubble on the chart is clicked, a text box pops up with the description of the particular crisis that the bubble represents.
Once the bubble is clicked, the right hand side bar charts are populated with moves relevant to this scenario.
The left hand pane contains two text boxes. The lower one is particularly important, because the user is able to remove scenarios or add scenarios (screen #2). Removing scenarios is simple.
Adding scenarios brings up a wizard (screen #3). It also needs to be designed consistently with the front page of the app. The wizard has different clickable categories going down the column on the left and in a row on the top. The user can pick some or all of these categories.

Notes: The app should be designed for landscape mode only. The key to keep in mind is how the user will select bubbles on the chart. Right now, it is quite easy, but with the touchscreen it may be more complicated, so please keep that in mind when designing the chart (it should still be some version of the similar chart).
*As a first pass, please submit your idea of the concept (layout/colors/buttons) without the detailed design. We will choose 1-3 concepts and then the detailed work will take place with a much higher chance of a payout.
Updates

Thank you for the first two sketches. The second one by bertrand appears to be a bit more mobile app oriented, though we are still considering both and waiting for other submissions. One request, could you rework the sketches to include a bit more of dark blue as a background?  \

Bertrand, I think that the bubbles are too small and they are missing some volume effects. Could you make them a bit more prominent (and pick some form of dark blue background) and change the color to see if they will stand out better?
 

Industry/Entity Type

Financial

Requirements
Must have
• The general outline for the bubble chart must be retained. But the actual execution may differ significantly. We are open to seeing different ideas.
The winning design will also get a contract to design the rest of the application (2 more screens), which will be worth the same as the original design.

```html
<!DOCTYPE html>
<html lang="en">
<head>
<meta charset="utf-8">
<title>Ledgerwise 540 for Tavlo – Mobile Screens</title>
<link href="https://fonts.googleapis.com/css2?family=Open+Sans:wght@400;600&display=swap" rel="stylesheet">
<style>
  :root {
    --page-bg: #e9e9eb;
    --screen-bg: #1b1c1e;
    --screen-edge: #0f1011;
    --tabbar-bg: #161718;
    --tab-active: #232427;
    --text: #f2f2f2;
    --text-muted: #a7a9ad;
    --text-link: #8f9296;
    --grid-bg: #202225;
    --grid-line: #2b2d31;
    --blue: #3a8fe0;
    --blue-deep: #1b5ca8;
    --orange: #e28a1c;
    --orange-deep: #9a5a0c;
    --bar-blue: #2f7fd4;
    --bar-orange: #e2561e;
    --field-bg: #141516;
    --scroll: #d8d8d8;
  }
  * { box-sizing: border-box; margin: 0; padding: 0; }
  html, body { width: 1200px; height: 715px; overflow: hidden; }
  body {
    background: var(--page-bg);
    font-family: "Open Sans", Arial, sans-serif;
    color: var(--text);
    position: relative;
  }
  .slot { position: absolute; width: 560px; height: 318.5px; }
  .slot--tl { left: 30px; top: 30px; }
  .slot--tr { left: 610px; top: 30px; }
  .slot--bl { left: 30px; top: 378px; }
  .slot--br { left: 610px; top: 378px; }

  .screen {
    position: absolute; left: 0; top: 0;
    width: 480px; height: 273px;
    transform: scale(1.1667); transform-origin: 0 0;
    background: var(--screen-bg);
    border: 1px solid var(--screen-edge);
    overflow: hidden;
  }
  .tabbar {
    position: absolute; left: 0; top: 0; width: 100%; height: 38px;
    background: var(--tabbar-bg);
  }
  .back-button {
    position: absolute; left: 12px; top: 12px; width: 58px; height: 21px;
    background: linear-gradient(#5aa3e6, #2f76c4);
    border-radius: 2px;
    font-size: 7px; color: #d7e8fa; letter-spacing: .3px;
    line-height: 21px; padding-left: 20px;
  }
  .back-button::before {
    content: ""; position: absolute; left: 7px; top: 7px;
    border: 3.5px solid transparent; border-right: 4px solid #d7e8fa; border-left: 0;
  }
  .tab {
    position: absolute; top: 12px; height: 26px; line-height: 25px;
    font-size: 12px; color: var(--text); padding: 0 12px;
  }
  .tab--portfolio { left: 76px; }
  .tab--charts { left: 225px; }
  .tab--details { left: 311px; }
  .tab.is-active { background: var(--tab-active); }

  .axis-label { position: absolute; font-size: 9px; color: var(--text); }
  .axis-label--y { left: 14px; top: 148px; transform: translate(-50%, -50%) rotate(-90deg); left: 20px; white-space: nowrap; }
  .axis-label--x { top: 251px; }

  .chart-grid {
    position: absolute; top: 42px; height: 202px;
    background-color: var(--grid-bg);
    background-image:
      linear-gradient(var(--grid-line) 1px, transparent 1px),
      linear-gradient(90deg, var(--grid-line) 1px, transparent 1px);
    background-size: 11px 11px;
  }
  .chart-svg { position: absolute; left: 0; top: 0; }

  .scenario-panel { position: absolute; left: 346px; top: 50px; width: 120px; }
  .scenario-title { font-size: 11px; margin-bottom: 14px; }
  .metric { display: flex; font-size: 9.5px; margin-bottom: 8px; }
  .metric-value { width: 36px; text-align: right; margin-right: 6px; }
  .metric-name { color: var(--text-muted); line-height: 1.35; }
  .scrollbar { position: absolute; width: 2px; background: var(--scroll); border-radius: 1px; }

  .contrib { position: absolute; top: 46px; }
  .contrib-title { font-size: 11.5px; margin-bottom: 8px; }
  .contrib-row { position: relative; height: 22.6px; font-size: 9px; }
  .contrib-name { color: var(--text-link); text-decoration: underline; position: absolute; left: 0; top: 3px; }
  .contrib-value { position: absolute; right: 0; top: 2px; }
  .contrib-bar { position: absolute; bottom: 3px; height: 2px; }
  .contrib--high .contrib-bar { left: 0; background: var(--bar-blue); }
  .contrib--low .contrib-bar { right: 0; background: var(--bar-orange); }

  .settings { position: absolute; left: 0; top: 50px; width: 100%; }
  .field { position: absolute; left: 0; width: 100%; height: 22px; }
  .field-label { position: absolute; right: 329px; top: 4px; font-size: 9.5px; text-align: right; white-space: nowrap; }
  .select {
    position: absolute; left: 160px; width: 182px; height: 22px;
    background: var(--field-bg); font-size: 9.5px; line-height: 22px; padding-left: 12px;
  }
  .select-arrow {
    position: absolute; right: 2px; top: 4px; width: 14px; height: 14px;
    background: #d6d6d6; border-radius: 1px;
  }
  .select-arrow::after {
    content: ""; position: absolute; left: 4px; top: 5px;
    border: 3px solid transparent; border-top: 4px solid #333; border-bottom: 0;
  }
  .stepper { position: absolute; left: 163px; top: 1px; height: 18px; font-size: 9.5px; }
  .stepper-btn {
    position: absolute; top: 0; width: 17px; height: 17px; background: #d6d6d6;
    color: #222; font-size: 12px; line-height: 16px; text-align: center; font-weight: 600;
  }
  .stepper-value { position: absolute; left: 26px; top: 2px; }
  .checkbox-row { position: absolute; left: 160px; font-size: 9.5px; display: flex; align-items: center; }
  .checkbox { width: 6px; height: 6px; background: var(--blue); margin: 0 12px 0 3px; }
</style>
</head>
<body>

<!-- Scenario chart with detail panel -->
<div class="slot slot--tl">
  <section class="screen">
    <nav class="tabbar">
      <span class="back-button">BACK</span>
      <span class="tab tab--portfolio">SELECT PORTFOLIO</span>
      <span class="tab tab--charts is-active">CHARTS</span>
      <span class="tab tab--details">DETAILS</span>
    </nav>
    <div class="chart-grid" style="left:32px;width:308px;"></div>
    <svg class="chart-svg" width="480" height="273" aria-hidden="true">
      <defs>
        <radialGradient id="bubbleBlue" cx="38%" cy="32%" r="70%">
          <stop offset="0" stop-color="#7cc0ff"/><stop offset=".55" stop-color="#2f86dc"/><stop offset="1" stop-color="#164e92"/>
        </radialGradient>
        <radialGradient id="bubbleOrange" cx="38%" cy="32%" r="70%">
          <stop offset="0" stop-color="#ffc25e"/><stop offset=".6" stop-color="#d88316"/><stop offset="1" stop-color="#7f4a08"/>
        </radialGradient>
      </defs>
      <polygon points="36,77 42,73 42,81" fill="var(--blue)"/>
      <polygon points="36,154 42,150 42,158" fill="var(--orange)"/>
      <circle cx="131" cy="84" r="11" fill="url(#bubbleBlue)"/>
      <circle cx="313" cy="71" r="5" fill="url(#bubbleOrange)"/>
      <circle cx="275" cy="189" r="3.5" fill="url(#bubbleBlue)"/>
    </svg>
    <span class="axis-label axis-label--y">Correlation Surprise</span>
    <span class="axis-label axis-label--x" style="left:179px;">Loss</span>
    <aside class="scenario-panel">
      <h2 class="scenario-title" style="font-weight:400;">Stagflation Server</h2>
      <div class="metric"><span class="metric-value">-18.82</span><span class="metric-name">Loss</span></div>
      <div class="metric"><span class="metric-value">0.00</span><span class="metric-name">Plausibility</span></div>
      <div class="metric"><span class="metric-value">-18.82</span><span class="metric-name">Correlation<br>&nbsp;Surprise</span></div>
    </aside>
    <span class="scrollbar" style="left:468px;top:85px;height:120px;"></span>
  </section>
</div>

<!-- Full-width scenario chart -->
<div class="slot slot--tr">
  <section class="screen">
    <nav class="tabbar">
      <span class="back-button">BACK</span>
      <span class="tab tab--portfolio">SELECT PORTFOLIO</span>
      <span class="tab tab--charts is-active">CHARTS</span>
      <span class="tab tab--details">DETAILS</span>
    </nav>
    <div class="chart-grid" style="left:32px;width:435px;"></div>
    <svg class="chart-svg" width="480" height="273" aria-hidden="true">
      <polygon points="36,77 42,73 42,81" fill="var(--blue)"/>
      <polygon points="36,154 42,150 42,158" fill="var(--orange)"/>
      <circle cx="313" cy="71" r="5" fill="url(#bubbleOrange)"/>
      <circle cx="165" cy="104" r="3.5" fill="url(#bubbleBlue)"/>
      <circle cx="393" cy="104" r="3.5" fill="url(#bubbleBlue)"/>
      <circle cx="116" cy="185" r="5" fill="url(#bubbleOrange)"/>
      <circle cx="275" cy="189" r="3.5" fill="url(#bubbleBlue)"/>
    </svg>
    <span class="axis-label axis-label--y">Correlation Surprise</span>
    <span class="axis-label axis-label--x" style="left:179px;">Loss</span>
  </section>
</div>

<!-- Asset contributions -->
<div class="slot slot--bl">
  <section class="screen">
    <nav class="tabbar">
      <span class="back-button">BACK</span>
      <span class="tab tab--portfolio">SELECT PORTFOLIO</span>
      <span class="tab tab--charts">CHARTS</span>
      <span class="tab tab--details is-active">DETAILS</span>
    </nav>
    <div class="contrib contrib--high" style="left:18px;width:175px;">
      <h2 class="contrib-title" style="font-weight:400;">Assets Contribution 10 Highest</h2>
      <div class="contrib-row"><span class="contrib-name">KRV 6.505 02/12/67</span><span class="contrib-value">0.083</span><span class="contrib-bar" style="width:98px"></span></div>
      <div class="contrib-row"><span class="contrib-name">KRV 6.505 02/12/67</span><span class="contrib-value">0.083</span><span class="contrib-bar" style="width:90px"></span></div>
      <div class="contrib-row"><span class="contrib-name">KRV 6.505 02/12/67</span><span class="contrib-value">0.083</span><span class="contrib-bar" style="width:68px"></span></div>
      <div class="contrib-row"><span class="contrib-name">KRV 6.505 02/12/67</span><span class="contrib-value">0.083</span><span class="contrib-bar" style="width:56px"></span></div>
      <div class="contrib-row"><span class="contrib-name">KRV 6.505 02/12/67</span><span class="contrib-value">0.083</span><span class="contrib-bar" style="width:32px"></span></div>
      <div class="contrib-row"><span class="contrib-name">KRV 6.505 02/12/67</span><span class="contrib-value">0.083</span><span class="contrib-bar" style="width:40px"></span></div>
      <div class="contrib-row"><span class="contrib-name">KRV 6.505 02/12/67</span><span class="contrib-value">0.083</span><span class="contrib-bar" style="width:30px"></span></div>
      <div class="contrib-row"><span class="contrib-name">KRV 6.505 02/12/67</span><span class="contrib-value">0.083</span><span class="contrib-bar" style="width:22px"></span></div>
    </div>
    <span class="scrollbar" style="left:202px;top:78px;height:118px;"></span>
    <div class="contrib contrib--low" style="left:223px;width:173px;">
      <h2 class="contrib-title" style="font-weight:400;">Assets Contribution 10 Lowest</h2>
      <div class="contrib-row"><span class="contrib-name">KRV 6.505 02/12/67</span><span class="contrib-value">0.083</span><span class="contrib-bar" style="width:155px"></span></div>
      <div class="contrib-row"><span class="contrib-name">KRV 6.505 02/12/67</span><span class="contrib-value">0.083</span><span class="contrib-bar" style="width:148px"></span></div>
      <div class="contrib-row"><span class="contrib-name">KRV 6.505 02/12/67</span><span class="contrib-value">0.083</span><span class="contrib-bar" style="width:88px"></span></div>
      <div class="contrib-row"><span class="contrib-name">KRV 6.505 02/12/67</span><span class="contrib-value">0.083</span><span class="contrib-bar" style="width:80px"></span></div>
      <div class="contrib-row"><span class="contrib-name">KRV 6.505 02/12/67</span><span class="contrib-value">0.083</span><span class="contrib-bar" style="width:56px"></span></div>
      <div class="contrib-row"><span class="contrib-name">KRV 6.505 02/12/67</span><span class="contrib-value">0.083</span><span class="contrib-bar" style="width:48px"></span></div>
      <div class="contrib-row"><span class="contrib-name">KRV 6.505 02/12/67</span><span class="contrib-value">0.083</span><span class="contrib-bar" style="width:36px"></span></div>
      <div class="contrib-row"><span class="contrib-name">KRV 6.505 02/12/67</span><span class="contrib-value">0.083</span><span class="contrib-bar" style="width:28px"></span></div>
    </div>
    <span class="scrollbar" style="left:405px;top:78px;height:118px;"></span>
  </section>
</div>

<!-- Portfolio selection -->
<div class="slot slot--br">
  <section class="screen">
    <nav class="tabbar">
      <span class="back-button">BACK</span>
      <span class="tab tab--portfolio is-active">SELECT PORTFOLIO</span>
      <span class="tab tab--charts">CHARTS</span>
      <span class="tab tab--details">DETAILS</span>
    </nav>
    <div class="settings">
      <div class="field" style="top:1px;"><span class="field-label">Portfolio Date</span><div class="select">Portfolio Date<span class="select-arrow"></span></div></div>
      <div class="field" style="top:33px;"><span class="field-label">Portfolio</span><div class="select">Select Portfolio<span class="select-arrow"></span></div></div>
      <div class="field" style="top:65px;"><span class="field-label">Currency</span><div class="select">USD<span class="select-arrow"></span></div></div>
      <div class="field" style="top:97px;"><span class="field-label">Weight Type</span><div class="select">Active<span class="select-arrow"></span></div></div>
      <div class="field" style="top:127px;"><span class="field-label">Model</span><div class="select">Vextrion<span class="select-arrow"></span></div></div>
      <div class="field" style="top:160px;"><span class="field-label">Loss Threshold</span>
        <div class="stepper"><span class="stepper-btn" style="left:0">−</span><span class="stepper-value">-10</span><span class="stepper-btn" style="left:62px">+</span></div>
      </div>
      <div class="checkbox-row" style="top:191px;"><span class="checkbox"></span>Only Key Scenarios</div>
    </div>
    <span class="scrollbar" style="left:464px;top:66px;height:116px;"></span>
  </section>
</div>

</body>
</html>
```